Marlowe's Larder home based food retailer

I need a label for my new home based business making granola. Other products like cookies, jams and relishes in future.

I imagine the original logo in dark or mid (dusty) blue with white printing.

A logo that can be easily be recognised across a variety of product lines. IE: the same design that can be different colours for other flavours of granola. EG: green for fig & pistachio, red for cherry & chocolate

The granola will be packaged in resealable kraft paper bags.

The logo and product name will be on the front and other information on the back. IE: ingredients, nutritional panel, contact details. See below

The whole label will measure 210mm (L) x 80mm (W), with 80mm on the front and 130mm on the back. See attached

FRONT:
Marlowe's Larder
ORIGINAL GRANOLA
400g

BACK:
Marlowe's Larder
ORIGINAL GRANOLA
Delicious, all natural granola made in the beautiful Macedon Ranges. Serve with your choice of milk, fruit or yoghurt. Store in an airtight container.

INGREDIENTS:
Oats (print in bold), honey, coconut oil, pumpkin seeds, almonds(print in bold), sultanas, sunflower seeds, linseeds, vanilla extract, cinnamon, sea salt.
Contains gluten and nuts (print in bold)

Made in Australia using local and imported ingredients.

Contact:
marloweslarder.com.au
info@marloweslarder.com.au
facebook logo
instagram logo

NUTRITIONAL PANEL (see attached)

Many thanks,
Marlowe

Target Market(s)

For those who are seeking a locally homemade, wholesome breakfast or snack. Cafes, market stalls, fruit & veg distributorss

Industry/Entity Type

granola production

Logo Text

Marlowe's Larder. Original Granola. 400g

Logo styles of interest
Pictorial/Combination Logo
Wordmark Logo
Font styles to use
Serif
Script

Colors
0054AA
0677BA
7BADD7
CADEEF
E8F1F8
00AB8E
00BBA5
67D7C9
C6EFE9
E9F9F6
EE7325
F08F49
F5BC92
FAE3D3
FDF4ED
EB3D1F
EC4F4E
F09395
F8D3D4
FCEDEE

Requirements
Must have
• Pretty, yet simple logo
Nice to have
• A variety of options with background design or a little symbol. Prefer dusty colours
Should not have
• too fancy or fussy design, bright colours

```html
<!DOCTYPE html>
<html lang="en">
<head>
<meta charset="utf-8">
<title>Marlowe's Larder – Granola Label Options</title>
<link href="https://fonts.googleapis.com/css2?family=Allura&family=Cormorant+Garamond:wght@500;600&family=Poppins:wght@400;600&display=swap" rel="stylesheet">
<style>
  :root {
    --page: #ffffff;
    --label: #5c6c88;
    --label-deep: #3f4d68;
    --ink: #ffffff;
    --ink-soft: rgba(255,255,255,0.75);
    --caption: #5c6c88;
    --panel: #ffffff;
    --panel-ink: #1f2838;
  }
  * { box-sizing: border-box; margin: 0; padding: 0; }
  html, body { width: 1200px; height: 1200px; overflow: hidden; background: var(--page); }
  .canvas { position: relative; width: 1200px; height: 1200px; }

  .label {
    position: absolute; top: 248px; width: 273px; height: 713px;
    background: var(--label); color: var(--ink);
    font-family: "Poppins", sans-serif;
  }
  .label--flowers { left: 217px; }
  .label--leaves { left: 720px; }

  /* back panel, printed upside down above the fold */
  .back {
    position: absolute; left: 0; top: 0; width: 273px; height: 444px;
    transform: rotate(180deg);
    padding: 10px 12px 0;
    display: flex; flex-direction: column; align-items: center; text-align: center;
  }
  .dots { width: 100%; border-top: 1px dotted var(--ink-soft); }
  .back__title {
    margin-top: 12px;
    font-family: "Cormorant Garamond", serif; font-weight: 600;
    font-size: 21px; letter-spacing: 0.5px; line-height: 1;
  }
  .back__sub {
    font-family: "Cormorant Garamond", serif; font-weight: 500;
    font-size: 11px; letter-spacing: 1.5px; margin-top: 4px;
  }
  .back__weight { font-size: 7px; margin-top: 3px; }
  .back__desc { font-size: 6.5px; line-height: 1.55; margin: 7px 0 12px; padding: 0 8px; }
  .back__heading { font-size: 8px; letter-spacing: 0.5px; margin: 10px 0 4px; }
  .back__ingredients { font-size: 6.5px; line-height: 1.55; padding: 0 8px; }
  .back__ingredients b, .back__allergen { font-weight: 600; }
  .back__allergen { font-size: 7px; margin: 8px 0 12px; }
  .origin {
    margin-top: 10px; width: 238px; height: 28px;
    border: 1px solid var(--ink); border-radius: 3px;
    display: flex; align-items: center; gap: 8px; padding: 0 8px;
    font-size: 5.5px; text-align: left;
  }
  .origin__badge { width: 14px; height: 14px; background: var(--ink); flex: none; }
  .back__foot {
    width: 100%; margin-top: 16px;
    display: flex; justify-content: space-between; align-items: flex-end;
  }
  .contact { font-size: 5.5px; text-align: left; line-height: 1.8; }
  .contact__social { display: flex; gap: 5px; margin-top: 4px; }
  .contact__social span { width: 8px; height: 8px; border-radius: 50%; background: var(--ink); }
  .nutrition {
    width: 133px; background: var(--panel); color: var(--panel-ink);
    padding: 4px 5px; font-size: 5px; text-align: left;
  }
  .nutrition__title { font-weight: 600; font-size: 6px; border-bottom: 1px solid var(--panel-ink); padding-bottom: 2px; }
  .nutrition table { width: 100%; border-collapse: collapse; margin-top: 2px; }
  .nutrition td { padding: 0.6px 0; }
  .nutrition td + td { text-align: right; }
  .nutrition .head td { border-top: 1px solid var(--panel-ink); border-bottom: 1px solid var(--panel-ink); }

  /* front panel */
  .front {
    position: absolute; left: 0; top: 444px; width: 273px; height: 269px;
    border-top: 1px dotted var(--ink-soft);
  }
  .wreath { position: absolute; left: 22px; top: 22px; width: 176px; height: 176px; }
  .label--leaves .wreath { left: 40px; }
  .brand {
    position: absolute; left: 0; top: 66px; width: 232px; text-align: center;
    font-family: "Allura", cursive; font-size: 38px; line-height: 0.85;
  }
  .label--leaves .brand { width: 250px; }
  .product {
    position: absolute; left: 0; top: 167px; width: 232px; text-align: center;
    font-family: "Cormorant Garamond", serif; font-weight: 500;
    font-size: 11px; letter-spacing: 2px; line-height: 1.15;
  }
  .label--leaves .product { width: 250px; }
  .product__rule { display: block; width: 100px; margin: 1px auto; border-top: 1px solid var(--ink); }
  .product__weight { display: block; font-family: "Poppins", sans-serif; font-size: 9px; letter-spacing: 0; margin-top: 5px; }

  .caption {
    position: absolute; left: 0; top: 1090px; width: 1200px; text-align: center;
    font-family: "Poppins", sans-serif; font-size: 17.5px; line-height: 1.5; color: var(--caption);
  }
</style>
</head>
<body>
<div class="canvas">

  <!-- option A: flowers kept, oats removed -->
  <div class="label label--flowers">
    <div class="back">
      <div class="dots"></div>
      <div class="back__title">MARLOWE'S LARDER</div>
      <div class="back__sub">ORIGINAL GRANOLA</div>
      <div class="back__weight">400g</div>
      <p class="back__desc">Delicious, all natural granola made in the beautiful Macedon Ranges. Serve with your choice of milk, fruit or yoghurt. Store in an airtight container.</p>
      <div class="dots"></div>
      <div class="back__heading">INGREDIENTS:</div>
      <p class="back__ingredients"><b>Oats</b>, honey, coconut oil, pumpkin seeds, <b>almonds</b>, sultanas, sunflower seeds, linseeds, vanilla extract, cinnamon, sea salt.</p>
      <p class="back__allergen">Contains gluten and nuts.</p>
      <div class="dots"></div>
      <div class="origin"><span class="origin__badge"></span>Made in Australia using local and imported ingredients.</div>
      <div class="back__foot">
        <div class="contact">
          marloweslarder.com.au<br>info@marloweslarder.com.au
          <div class="contact__social"><span></span><span></span></div>
        </div>
        <div class="nutrition">
          <div class="nutrition__title">NUTRITION INFORMATION</div>
          <div>Servings per package: 8<br>Serving size: 50 g</div>
          <table>
            <tr class="head"><td></td><td>Per Serving</td><td>Per 100g</td></tr>
            <tr><td>Energy</td><td>972 kJ</td><td>1940 kJ</td></tr>
            <tr><td>Protein</td><td>5.1 g</td><td>10.2 g</td></tr>
            <tr><td>Total Fat</td><td>13.1 g</td><td>26.2 g</td></tr>
            <tr><td>– saturated</td><td>5.2 g</td><td>10.4 g</td></tr>
            <tr><td>Carbohydrate</td><td>21.9 g</td><td>43.8 g</td></tr>
            <tr><td>– sugars</td><td>11.3 g</td><td>22.5 g</td></tr>
            <tr><td>Sodium</td><td>25 mg</td><td>50 mg</td></tr>
          </table>
        </div>
      </div>
    </div>
    <div class="front">
      <svg class="wreath" viewBox="0 0 176 176" role="img" aria-label="Botanical wreath of flowers and berries framing the name">
        <circle cx="88" cy="88" r="78" fill="none" stroke="var(--label-deep)" stroke-width="9" opacity="0.8"/>
      </svg>
      <div class="brand">Marlowe's<br>Larder</div>
      <div class="product"><span class="product__rule"></span>ORIGINAL<br>GRANOLA<span class="product__rule"></span><span class="product__weight">400g</span></div>
    </div>
  </div>

  <!-- option B: leaves kept, flowers removed -->
  <div class="label label--leaves">
    <div class="back">
      <div class="dots"></div>
      <div class="back__title">MARLOWE'S LARDER</div>
      <div class="back__sub">ORIGINAL GRANOLA</div>
      <div class="back__weight">400g</div>
      <p class="back__desc">Delicious, all natural granola made in the beautiful Macedon Ranges. Serve with your choice of milk, fruit or yoghurt. Store in an airtight container.</p>
      <div class="dots"></div>
      <div class="back__heading">INGREDIENTS:</div>
      <p class="back__ingredients"><b>Oats</b>, honey, coconut oil, pumpkin seeds, <b>almonds</b>, sultanas, sunflower seeds, linseeds, vanilla extract, cinnamon, sea salt.</p>
      <p class="back__allergen">Contains gluten and nuts.</p>
      <div class="dots"></div>
      <div class="origin"><span class="origin__badge"></span>Made in Australia using local and imported ingredients.</div>
      <div class="back__foot">
        <div class="contact">
          marloweslarder.com.au<br>info@marloweslarder.com.au
          <div class="contact__social"><span></span><span></span></div>
        </div>
        <div class="nutrition">
          <div class="nutrition__title">NUTRITION INFORMATION</div>
          <div>Servings per package: 8<br>Serving size: 50 g</div>
          <table>
            <tr class="head"><td></td><td>Per Serving</td><td>Per 100g</td></tr>
            <tr><td>Energy</td><td>972 kJ</td><td>1940 kJ</td></tr>
            <tr><td>Protein</td><td>5.1 g</td><td>10.2 g</td></tr>
            <tr><td>Total Fat</td><td>13.1 g</td><td>26.2 g</td></tr>
            <tr><td>– saturated</td><td>5.2 g</td><td>10.4 g</td></tr>
            <tr><td>Carbohydrate</td><td>21.9 g</td><td>43.8 g</td></tr>
            <tr><td>– sugars</td><td>11.3 g</td><td>22.5 g</td></tr>
            <tr><td>Sodium</td><td>25 mg</td><td>50 mg</td></tr>
          </table>
        </div>
      </div>
    </div>
    <div class="front">
      <svg class="wreath" viewBox="0 0 176 176" role="img" aria-label="Partial botanical wreath of leaves and oat sprigs around the name">
        <path d="M120 14 A78 78 0 0 1 120 162" fill="none" stroke="var(--label-deep)" stroke-width="9" opacity="0.8"/>
        <path d="M30 140 A78 78 0 0 0 110 164" fill="none" stroke="var(--label-deep)" stroke-width="7" opacity="0.8"/>
      </svg>
      <div class="brand">Marlowe's<br>Larder</div>
      <div class="product"><span class="product__rule"></span>ORIGINAL<br>GRANOLA<span class="product__rule"></span><span class="product__weight">400g</span></div>
    </div>
  </div>

  <p class="caption">5. Can I see what it looks like with partial botanicals? Ie: Remove the oat grains<br>on one design and remove the flowers/leaves on the other.</p>
</div>
</body>
</html>
```